The Biggest Party Of The Year!

Copper Lantern Presents

The Harvest Moon Splash Bash 2015

August 29TH

Dune Deck Lounge
7831 East Marlow Blvd
Odessa, TX 79384

18 & UP

9PM-2AM

Tickets Go On Sale

August 1, 2015

Will Sell Out! Get You Tickets

Music
Hip-Hop & Dance

Live in the Mix
TBA DJ Line UP

Attire
Beach Wear

Sponsors Contact
Brenna Voskuil
432.555.0187

Drinks, Lights and Bass

$500 Twerk Contest

Foam Party

Beer Pong Tournament

Target Market(s)

18 up college Students & Party Goers

Industry/Entity Type

Party Planning

Font styles to use
Sans Serif

Requirements
Must have
• Atlot of Energy, Must Create Urgency. Red, Blue & Black Color Scheme. Beach Theme. Should be in a invitation form.

```html
<!DOCTYPE html>
<html lang="en">
<head>
<meta charset="utf-8">
<title>The Harvest Moon Splash Bash 2015</title>
<link rel="stylesheet" href="https://fonts.googleapis.com/css2?family=Oswald:wght@500;700&family=Roboto+Condensed:wght@400;700&display=swap">
<style>
  :root {
    --night: #0c0626;
    --deep-violet: #2a0b5c;
    --violet: #6a1fb8;
    --magenta: #d02ec6;
    --hot-pink: #ff3fae;
    --title-glow: #ffd6f4;
    --soft-pink: #f4b8ff;
    --lilac: #c9a6ff;
    --white: #ffffff;
    --lime: #6dff2e;
    --badge: #b24ae6;
    --shadow: #1a0530;
  }
  html, body {
    margin: 0;
    padding: 0;
    overflow: hidden;
    background: var(--night);
  }
  .flyer {
    position: relative;
    width: 849px;
    height: 1200px;
    overflow: hidden;
    font-family: "Roboto Condensed", Arial, sans-serif;
    color: var(--white);
  }
  .party-scene {
    position: absolute;
    inset: 0;
    background:
      /* dark palm fronds framing the top corners */
      radial-gradient(ellipse 300px 260px at 90px 120px, rgba(8,3,22,0.95) 0%, rgba(8,3,22,0.7) 45%, transparent 100%),
      radial-gradient(ellipse 360px 240px at 620px 70px, rgba(8,3,22,0.92) 0%, rgba(8,3,22,0.55) 50%, transparent 100%),
      radial-gradient(ellipse 160px 300px at 830px 300px, rgba(8,3,22,0.8) 0%, transparent 100%),
      /* dancing crowd silhouettes in the lower half */
      radial-gradient(ellipse 260px 420px at 470px 860px, rgba(20,6,40,0.92) 0%, rgba(20,6,40,0.6) 55%, transparent 100%),
      radial-gradient(ellipse 200px 380px at 740px 900px, rgba(20,6,40,0.88) 0%, rgba(20,6,40,0.45) 60%, transparent 100%),
      radial-gradient(ellipse 620px 260px at 50% 1130px, rgba(10,4,30,0.97) 0%, rgba(10,4,30,0.6) 60%, transparent 100%),
      /* stage lights and bokeh glow */
      radial-gradient(circle at 330px 470px, rgba(255,245,255,0.95) 0%, rgba(255,170,240,0.75) 8%, rgba(230,80,220,0.4) 22%, transparent 40%),
      radial-gradient(circle at 60px 560px, rgba(255,150,200,0.75) 0%, rgba(255,90,190,0.35) 14%, transparent 28%),
      radial-gradient(circle at 110px 720px, rgba(255,170,140,0.55) 0%, transparent 18%),
      radial-gradient(circle at 800px 640px, rgba(255,230,255,0.8) 0%, rgba(240,120,240,0.35) 12%, transparent 26%),
      radial-gradient(circle at 720px 240px, rgba(140,80,255,0.6) 0%, transparent 30%),
      linear-gradient(165deg, var(--deep-violet) 0%, var(--violet) 30%, var(--magenta) 52%, var(--violet) 72%, var(--deep-violet) 88%, var(--night) 100%);
  }
  .presenter {
    position: absolute;
    top: 40px;
    left: 0;
    width: 100%;
    text-align: center;
    font-family: "Oswald", Arial, sans-serif;
    font-weight: 500;
    font-size: 30px;
    letter-spacing: 6px;
    text-transform: uppercase;
  }
  .event-title {
    position: absolute;
    top: 218px;
    left: 80px;
    width: 720px;
    margin: 0;
    text-align: center;
    font-family: "Oswald", Arial, sans-serif;
    font-weight: 700;
    font-size: 70px;
    line-height: 80px;
    text-transform: uppercase;
    color: var(--hot-pink);
    transform: rotate(-5deg);
    transform-origin: center;
    text-shadow: 0 0 4px var(--title-glow), 0 0 12px var(--title-glow), 2px 3px 0 var(--shadow);
  }
  .hours {
    position: absolute;
    top: 388px;
    left: 700px;
    font-size: 16px;
    font-weight: 700;
    color: var(--lime);
  }
  .event-date {
    position: absolute;
    top: 405px;
    left: 312px;
    font-family: "Oswald", Arial, sans-serif;
    font-weight: 700;
    font-size: 64px;
    line-height: 80px;
    text-transform: uppercase;
    transform: rotate(-4deg);
    text-shadow: 2px 3px 6px var(--shadow);
  }
  .contest-badge {
    position: absolute;
    top: 496px;
    left: 508px;
    width: 146px;
    height: 146px;
    border-radius: 50%;
    background: var(--badge);
    display: flex;
    flex-direction: column;
    align-items: center;
    justify-content: center;
    text-align: center;
  }
  .contest-prize {
    font-family: "Oswald", Arial, sans-serif;
    font-weight: 700;
    font-size: 46px;
    line-height: 50px;
    color: var(--lime);
  }
  .contest-name {
    font-size: 15px;
    font-weight: 700;
    color: var(--lime);
  }
  .highlights {
    position: absolute;
    top: 762px;
    left: 64px;
    width: 240px;
    margin: 0;
    padding: 0;
    list-style: none;
    text-align: center;
    font-size: 17px;
    font-weight: 700;
    line-height: 23px;
    text-shadow: 1px 1px 3px var(--shadow);
  }
  .ticket-call {
    position: absolute;
    top: 1088px;
    left: 0;
    width: 100%;
    text-align: center;
    font-size: 25px;
    font-weight: 700;
  }
  .venue-line, .sponsor-line {
    position: absolute;
    left: 0;
    width: 100%;
    text-align: center;
    font-size: 15px;
    color: var(--lilac);
  }
  .venue-line { top: 1130px; }
  .sponsor-line { top: 1160px; }
</style>
</head>
<body>
<main class="flyer">
  <div class="party-scene" role="img" aria-label="Beach party scene with dark palm leaves framing the top, bright purple and pink club lights with bokeh, and a dancing crowd in silhouette with raised hands"></div>

  <div class="presenter">Copper Lantern Presents</div>

  <h1 class="event-title">The Harvest Moon<br>Splash Bash 2015</h1>
  <div class="hours">9PM-2AM</div>

  <div class="event-date">August 29th</div>

  <div class="contest-badge">
    <span class="contest-prize">$500</span>
    <span class="contest-name">Twerk Contest</span>
  </div>

  <ul class="highlights">
    <li>Dune Deck Lounge</li>
    <li>Will Sell Out! Get You Tickets</li>
    <li>Music</li>
    <li>Hip-Hop &amp; Dance</li>
    <li>Live in the Mix</li>
    <li>TBA DJ Line UP</li>
    <li>Attire Beach Wear</li>
    <li>Drinks, Lights and Bass</li>
    <li>Foam Party</li>
    <li>Beer Pong Tournament</li>
  </ul>

  <div class="ticket-call">Tickets Go On Sale August 1, 2015</div>
  <div class="venue-line">7831 East Marlow Blvd Odessa, TX 79384 18 &amp; UP</div>
  <div class="sponsor-line">Sponsors Contact Brenna Voskuil 432.555.0187</div>
</main>
</body>
</html>
```